HVRT LLP website - revamping our website after 23 years

Our website needs a complete overhaul. The purpose of this exercise is to provide us with your vision of what you think the website should look like. We don't need the website to be created or coded. Just need creative designs.

We have a four sites that we would like to base our website on;

We like the simplicity of Ravelstoke, the style of Pemberly Adair and Quillfeather.

http://www.pemberlyadair.example/en/toronto-ontario/
http://www.ravelstoke.example/
vintquillfeather.example
http://www.brindlemoor.example/our-professionals.html

We have a logo that we would like to use which will be attached below. We need to keep our website looking very professional as we have a large number of high net worth clients.
Updates

Hi, We've received some good website designs but they appear to be the same type of template websites we've received in the past - this is not what we're looking for. What we want is a unique website that is modelled on the following three company websites: http://www.ravelstoke.example/ www.vintquillfeather.example/ http://www.pemberlyadair.example/en/toronto-ontario/

Thank you everyone for your designs. I will be posting updates and my comments on the various designs in the next day - I want to thank you for the creative designs I see. I thought i would explain a bit about our firm and perhaps it can help when you design the theme of our website: - Our firm is like a family and our clients are truly like our friends. We have close knit relationships in and outside of the office with staff and clients. - We are an 'out of the box' type of firm. We operate differently than most firms and that's a differentiating factor in what makes us who we are - Our slogan is "Count on us" which is a testament to the way we run our practice - We would like an open, fresh, clean look to our website - we don't want the landing page to be overly long or complex because we have limited time to update the website and limited content That's it for the time being - when things come to mind I will post them here.

Can we try a design as follows: - make the website look very similar to www.ravelstoke.example - use the same background colour - Keep the same black top but insert our logo - incorporate some of the content from our current website www.hvrt-ca.example

I have been away dealing with a personal matter. I will look into these websites tomorrow afternoon and provide more feedback / info on the top designer. Thank you

Hi designers, I want to apologize for the delay. I plan on wrapping things up within the next few days. I will go through a few of the top designs and offer my comments. Thank you for your patience.

Target Market(s)

Mainly our current clients - We have a large number of high net worth individuals as clients.

Industry/Entity Type

Accounting

Number of Pages Required

1 page

Requirements
Must have
• Please model website on the websites indicated above.
• Our current website is www.hvrt-ca.example. It's dark, cluttered and not inviting. We want a fresh, clean website. Please incorporate the logo's attached below.

```html
<!DOCTYPE html>
<html lang="en">
<head>
<meta charset="utf-8">
<title>HVRT LLP – Chartered Accountants</title>
<link rel="stylesheet" href="https://fonts.googleapis.com/css2?family=Raleway:wght@400;500&display=swap">
<style>
  :root {
    --header-bg: #404349;
    --nav-text: #ffffff;
    --nav-active: #3a9fd6;
    --page-bg: #f7f7f7;
    --body-text: #555a60;
    --heading: #4b2d8f;
    --accent-green: #7cc242;
    --band: rgba(184, 88, 138, 0.92);
    --white: #ffffff;
    --footer-text: #4a4d52;
  }
  * { box-sizing: border-box; margin: 0; padding: 0; }
  html, body {
    width: 1200px; height: 800px; overflow: hidden;
    background: var(--white);
    font-family: "Raleway", sans-serif;
  }
  .site-header {
    position: absolute; left: 0; top: 0; width: 1200px; height: 120px;
    background: var(--header-bg);
  }
  .brand {
    position: absolute; left: 132px; top: 28px;
    display: flex; align-items: center; gap: 16px;
    color: var(--white); font-size: 40px; font-weight: 500; letter-spacing: 1px;
  }
  .brand-square { width: 64px; height: 64px; background: var(--accent-green); }
  .main-nav {
    position: absolute; right: 132px; top: 0; height: 120px;
    display: flex; align-items: center; gap: 47px;
  }
  .main-nav a {
    position: relative; color: var(--nav-text); text-decoration: none;
    font-size: 14.5px; line-height: 120px; display: block;
  }
  .main-nav a.is-active::after {
    content: ""; position: absolute; left: -16px; right: -16px; bottom: 0;
    height: 4px; background: var(--nav-active);
  }
  .hero {
    position: absolute; left: 0; top: 120px; width: 1200px; height: 484px;
    background: var(--page-bg);
  }
  .hero-photo {
    position: absolute; left: 460px; top: 0; width: 608px; height: 484px;
    background:
      linear-gradient(90deg, var(--page-bg) 0%, rgba(247,247,247,0) 40%),
      linear-gradient(160deg, #e9ecef 0%, #cfd4d8 35%, #9ea4aa 60%, #dfe2e5 100%);
  }
  .hero-copy { position: absolute; left: 132px; top: 72px; width: 500px; }
  .hero-title {
    display: flex; align-items: center; gap: 8px;
    color: var(--heading); font-size: 24px; font-weight: 400; letter-spacing: 0.3px;
  }
  .hero-title::before {
    content: ""; width: 5px; height: 18px; background: var(--accent-green);
  }
  .hero-copy p {
    color: var(--body-text); font-size: 13.8px; line-height: 24px; margin-top: 21px;
  }
  .hero-copy p + p { margin-top: 21px; }
  .services-band {
    position: absolute; left: 132px; top: 470px; width: 936px; height: 134px;
    background: var(--band);
  }
  .service {
    position: absolute; top: 34px; width: 280px; text-align: center;
    color: var(--white); font-size: 17.5px;
  }
  .service svg { display: block; margin: 0 auto 14px; }
  .band-arrow { position: absolute; top: 50px; }
  .site-footer {
    position: absolute; left: 132px; top: 624px; width: 936px;
    display: flex; justify-content: space-between;
    color: var(--footer-text); font-size: 13px;
  }
  .site-footer a { color: var(--footer-text); text-decoration: none; }
  .footer-links span { margin: 0 6px; }
</style>
</head>
<body>
  <header class="site-header">
    <div class="brand"><span class="brand-square"></span>HVRT LLP</div>
    <nav class="main-nav">
      <a class="is-active" href="#">Home</a>
      <a href="#">About HVRT</a>
      <a href="#">Services</a>
      <a href="#">Library</a>
      <a href="#">Links</a>
      <a href="#">Contact Us</a>
    </nav>
  </header>

  <section class="hero">
    <div class="hero-photo" role="img" aria-label="Blurred professionals walking through a bright office corridor"></div>
    <div class="hero-copy">
      <h1 class="hero-title">INVALUABLE EXPERIENCE</h1>
      <p>HVRT, Harlow Vance Redding Thorne LLP Chartered Accountants, is a full-service, public accounting firm, primarily serving the small and mid-size, entrepreneurial business and professional sectors in Toronto, Canada.</p>
      <p>HVRT's experienced partners and professional, support staff strive to provide accounting and advisory services using an invaluable personal approach, designed to meet all your accounting requirements.</p>
    </div>
  </section>

  <section class="services-band">
    <svg class="band-arrow" style="left:30px" width="20" height="38" viewBox="0 0 20 38" fill="none" stroke="#fff" stroke-width="1.5"><path d="M18 1 L2 19 L18 37"/></svg>
    <div class="service" style="left:43px">
      <svg width="26" height="28" viewBox="0 0 26 28" fill="none" stroke="#fff" stroke-width="1.6">
        <rect x="1" y="1" width="24" height="26" rx="3"/><line x1="1" y1="8" x2="25" y2="8"/>
        <circle cx="7" cy="14" r="1.6"/><circle cx="13" cy="14" r="1.6"/><circle cx="19" cy="14" r="1.6"/>
        <circle cx="7" cy="21" r="1.6"/><circle cx="13" cy="21" r="1.6"/><circle cx="19" cy="21" r="1.6"/>
      </svg>
      Accounting &amp; Auditing
    </div>
    <div class="service" style="left:328px">
      <svg width="18" height="28" viewBox="0 0 18 28" fill="none" stroke="#fff" stroke-width="1.6">
        <path d="M9 1 A8 8 0 0 1 13 16 L13 19 L5 19 L5 16 A8 8 0 0 1 9 1 Z"/>
        <line x1="5" y1="22" x2="13" y2="22"/><line x1="6" y1="25" x2="12" y2="25"/><line x1="9" y1="10" x2="9" y2="19"/>
      </svg>
      Business Advisory
    </div>
    <div class="service" style="left:608px">
      <svg width="28" height="28" viewBox="0 0 28 28" fill="none" stroke="#fff" stroke-width="1.6">
        <circle cx="14" cy="14" r="12.5"/><circle cx="14" cy="14" r="9.5"/>
        <path d="M19 9 L15.5 15.5 L9 19 L12.5 12.5 Z"/>
      </svg>
      Tax Planning &amp; Compliance
    </div>
    <svg class="band-arrow" style="left:890px" width="20" height="38" viewBox="0 0 20 38" fill="none" stroke="#fff" stroke-width="1.5"><path d="M2 1 L18 19 L2 37"/></svg>
  </section>

  <footer class="site-footer">
    <span>© 2015 HVRT Chartered Accountants. All rights reserved.</span>
    <span class="footer-links"><a href="#">Privacy Policy</a><span>|</span><a href="#">Sitemap</a></span>
  </footer>
</body>
</html>
```